Conference flyer

We need a flyer for a conference for the defence industry. The attached has been updated with new information using last years flyer. We would like something new and fresh. Please note the theme of the conference is 'a global environment'.

The final design should reflect the defence industry and manufacturing.

```html
<!DOCTYPE html>
<html lang="en">
<head>
<meta charset="utf-8">
<title>Defence Trade Controls Annual Conference – Pages 5 &amp; 6</title>
<link href="https://fonts.googleapis.com/css2?family=Roboto:ital,wght@0,300;0,400;0,700;1,400&display=swap" rel="stylesheet">
<style>
:root{
  --accent:#29a8e0;
  --rule:#5ec0ea;
  --ink:#222;
  --muted:#444;
  --paper:#fff;
  --bg:#fff;
  --office:#e6e6e6;
  --office-rule:#8a8a8a;
  --banner-light:#dfe6f1;
  --banner-dark:#7f97c6;
}
*{box-sizing:border-box;margin:0;padding:0}
html,body{width:1200px;height:1000px;overflow:hidden;background:var(--bg)}
body{position:relative;font-family:"Roboto",Arial,sans-serif;color:var(--ink)}
.page{position:absolute;top:117px;height:765px;background:var(--paper);border:1px solid #ddd}
.page--five{left:48px;width:566px}
.page--six{left:613px;width:541px}
.banner{position:absolute;top:26px;height:103px;width:489px;
  background:linear-gradient(135deg,var(--banner-light) 0%,var(--banner-dark) 100%)}
.page--five .banner{left:25px}
.page--six .banner{left:24px}
.section-title{position:absolute;font-weight:300;font-size:17px;color:var(--accent);letter-spacing:.1px}

/* General information table */
.info-table{position:absolute;left:25px;top:186px;width:489px;border-top:1px solid var(--rule)}
.info-row{display:grid;grid-template-columns:142px 1fr;align-items:center;border-bottom:1px solid var(--rule);font-size:8.6px;line-height:11.4px}
.info-row dt{font-weight:700}
.info-row dd{color:var(--muted);max-width:318px}
.info-row a{color:var(--accent);text-decoration:none}
.register-intro{position:absolute;left:25px;top:640px;font-size:8.6px;color:var(--muted)}
.contact-list{position:absolute;left:25px;top:660px;display:flex;font-size:8.6px}
.contact{display:flex;gap:12px;flex:none}
.contact--web{width:156px}
.contact--phone{width:134px}
.contact strong{display:block;margin-bottom:4px}
.contact span{color:var(--muted)}
.contact svg{width:19px;height:19px;margin-top:4px;flex:none}
.page-footer{position:absolute;left:25px;top:726px;width:489px;border-top:1px solid var(--rule);padding-top:8px;text-align:right;font-size:7.6px;color:var(--muted)}

/* Registration form */
.field-list{position:absolute;left:25px;top:183px;width:232px;list-style:none}
.field-list li{height:19.5px;border-bottom:1px solid var(--rule);font-size:8.6px;color:var(--muted);padding-top:4px}
.form-heading{font-weight:700;font-size:8.6px;color:var(--ink)}
.payment{position:absolute;left:25px;top:376px;width:240px;font-size:8.6px;color:var(--muted)}
.payment .form-heading{margin-bottom:6px}
.option{display:flex;align-items:center;gap:6px;height:21px}
.box{display:inline-block;width:9px;height:9px;border:1px solid var(--accent);flex:none}
.card-types{display:flex;height:21px;align-items:center;white-space:nowrap}
.card-types span{display:flex;align-items:center;gap:5px}
.card-types .type-a{margin-left:6px;width:78px}
.card-types .type-b{width:52px}
.payment .field-line{width:232px;height:19.5px;border-bottom:1px solid var(--rule);padding-top:4px}
.note{margin-top:10px;font-size:7.2px;font-style:italic;white-space:nowrap}
.modules{position:absolute;left:283px;top:187px;width:240px;font-size:8.6px;color:var(--muted)}
.module{display:grid;grid-template-columns:16px 1fr;margin-top:8px;line-height:13.5px}
.module:first-of-type{margin-top:10px}
.module .box{margin-top:2px}
.module b{color:var(--ink)}
.module .indent{padding-left:45px;display:block}
.training{position:absolute;left:283px;top:375px;width:240px;font-size:8.6px;color:var(--muted)}
.training p{margin:12px 0 10px;width:222px;line-height:13px}
.attendee{margin-bottom:11px;line-height:12px}
.attendee .picks{display:flex;align-items:center;gap:4px}
.attendee .picks .box{margin-right:4px}
.office{position:absolute;left:24px;top:603px;width:489px;height:136px;background:var(--office);padding:24px 13px 0}
.office .form-heading{font-size:8.6px;margin-bottom:6px}
.office .field-line{height:19.5px;border-bottom:1px solid var(--office-rule);font-size:8.6px;color:var(--muted);padding-top:4px}
</style>
</head>
<body>

<section class="page page--five">
  <div class="banner" role="img" aria-label="Banner photograph: keyboard keys printed with national flags"></div>
  <h2 class="section-title" style="left:25px;top:152px">General Information</h2>

  <dl class="info-table">
    <div class="info-row" style="height:44px"><dt>Conference Venue:</dt><dd>Harbourline Convention Centre<br>14 Quayside Street, Riverbank, 3610<br>Tel: (03) 9400 1200</dd></div>
    <div class="info-row" style="height:23px"><dt>Registration Fee Includes:</dt><dd style="max-width:none">Entrance to the conference, refreshments, lunch, reception event on the first evening.</dd></div>
    <div class="info-row" style="height:22px"><dt>Dress Code:</dt><dd>Business attire.</dd></div>
    <div class="info-row" style="height:42px"><dt>Accommodation and Travel:</dt><dd>Travel and accommodation are not included in the conference fees. We do not refund airfares or hotel expenses if the event is cancelled. Contact Harbourline Convention Centre for competitive prices.</dd></div>
    <div class="info-row" style="height:85px"><dt>Sponsorship Opportunities:</dt><dd>Sponsoring the Defence Trade Controls Conference 2015 is a fantastic way of raising your company's profile within this market and ceating greater awareness of your brand. Join us at the Defence Trade Controls Conference to promote new and existing products and service offerings in a high profile way amongst a select goup of other sponsors and exhibitors. Contact us at <a href="mailto:conference@dtcevents.org">conference@dtcevents.org</a> to find out more information.</dd></div>
    <div class="info-row" style="height:56px"><dt>Early Bird Prices:</dt><dd>Early bird prices only apply to conference registrations and post conference training module registrations that have been <i>paid in full</i> by midnight 1of the date the earlybird closes.</dd></div>
    <div class="info-row" style="height:57px"><dt>Cancellation and<br>Substitution Policy:</dt><dd>Cancellations must be advised in writing at least 30 days prior to the event. An administration fee of $250 (inc. GST) will be incurred for all cancellations. A refund will not be given within 30 days of the event. If a registered attendee is unable to attend, a replacement attendee is welcome.</dd></div>
    <div class="info-row" style="height:22px"><dt>Payment Terms:</dt><dd style="max-width:none">Payment must be made prior to the event or admittance will not be permitted.</dd></div>
    <div class="info-row" style="height:44px"><dt>Electronic Ticket:</dt><dd>You will recevie an electronic ticket when you register online – tickets must be presented upon entry.</dd></div>
  </dl>

  <h2 class="section-title" style="left:25px;top:604px">How To Register</h2>
  <p class="register-intro">Complete the registration form below and return it to us by:</p>
  <div class="contact-list">
    <div class="contact contact--web">
      <svg viewBox="0 0 20 20" aria-hidden="true"><g fill="none" stroke="#111" stroke-width="1.4"><circle cx="10" cy="10" r="8.5"/><ellipse cx="10" cy="10" rx="3.6" ry="8.5"/><path d="M1.5 10h17M3 5.5h14M3 14.5h14M10 1.5v17"/></g></svg>
      <div><strong>Web</strong><span>www.tradecontrolsforum.org</span></div>
    </div>
    <div class="contact contact--phone">
      <svg viewBox="0 0 20 20" aria-hidden="true"><path fill="#111" d="M2 6c0-2 3-3.5 8-3.5S18 4 18 6v1.6h-4V6.2c-1-.4-2.4-.6-4-.6s-3 .2-4 .6v1.4H2zM5.5 9h9l2.5 4.5V18H3v-4.5z"/><g fill="#fff"><circle cx="7.5" cy="12" r=".8"/><circle cx="10" cy="12" r=".8"/><circle cx="12.5" cy="12" r=".8"/><circle cx="7.5" cy="14.5" r=".8"/><circle cx="10" cy="14.5" r=".8"/><circle cx="12.5" cy="14.5" r=".8"/></g></svg>
      <div><strong>Phone</strong><span>+61 7 5300 1400</span></div>
    </div>
    <div class="contact">
      <svg viewBox="0 0 20 20" aria-hidden="true"><g fill="none" stroke="#111" stroke-width="1.3"><rect x="5" y="1.5" width="10" height="7"/><path d="M7 4h6M7 6h6"/><rect x="2" y="8.5" width="16" height="9" rx="1"/><path d="M5 13h10M5 15.5h10"/></g></svg>
      <div><strong>Fax</strong><span>+61 7 5300 1401</span></div>
    </div>
  </div>
  <footer class="page-footer">Defence Trade Controls Annual Conference &nbsp; 5</footer>
</section>

<section class="page page--six">
  <div class="banner" role="img" aria-label="Banner photograph: keyboard keys printed with national flags"></div>
  <h2 class="section-title" style="left:24px;top:152px">Conference Registration</h2>

  <ul class="field-list">
    <li>Attendee #1:</li><li>Attendee #2:</li><li>Attendee #3:</li><li>Attendee #4:</li>
    <li>Company:</li><li>Address:</li><li>Contact No.:</li><li>Email:</li><li>Dietary Needs:</li>
  </ul>

  <div class="payment">
    <p class="form-heading">Payment Method: (Please check)</p>
    <div class="option"><span class="box"></span>Invoice</div>
    <div class="option"><span class="box"></span>Credit Card*</div>
    <div class="card-types">Card Type:<span class="type-a"><span class="box"></span>Northcard</span><span class="type-b"><span class="box"></span>Vantage</span><span><span class="box"></span>Orbit</span></div>
    <div class="field-line">Card Name:</div>
    <div class="field-line">Card Number:</div>
    <div class="field-line">Expiry Date:</div>
    <div class="field-line">Cardholder Email:</div>
    <p class="note">* Credit card payments incur a 2.5% surcharge. Orbit incurs 3%.</p>
  </div>

  <div class="modules">
    <p class="form-heading">1/2 day Training Module/s:</p>
    <div class="module"><span class="box"></span><span>1 June 2015<br><b>Module 1:</b> Trade Controls for Beginners</span></div>
    <div class="module"><span class="box"></span><span>4 June 2015<br><b>Module 2:</b> Practical Management of Export<span class="indent">Control Reform</span></span></div>
    <div class="module"><span class="box"></span><span><b>Module 3:</b> Tips and Hints for Best<span class="indent">Practice Compliance</span></span></div>
    <div class="module"><span class="box"></span><span>5 June 2015<br><b>Module 4:</b> Making the Best of Commerce Exceptions</span></div>
  </div>

  <div class="training">
    <p class="form-heading" style="margin:0">Training Registration:</p>
    <p>Please tick which module each attendee would like to register for.</p>
    <div class="attendee">Attendee #1:<div class="picks">Module 1 <span class="box"></span> Module 2 <span class="box"></span> Module 3 <span class="box"></span> Module 4 <span class="box"></span></div></div>
    <div class="attendee">Attendee #2:<div class="picks">Module 1 <span class="box"></span> Module 2 <span class="box"></span> Module 3 <span class="box"></span> Module 4 <span class="box"></span></div></div>
    <div class="attendee">Attendee #3:<div class="picks">Module 1 <span class="box"></span> Module 2 <span class="box"></span> Module 3 <span class="box"></span> Module 4 <span class="box"></span></div></div>
    <div class="attendee">Attendee #4:<div class="picks">Module 1 <span class="box"></span> Module 2 <span class="box"></span> Module 3 <span class="box"></span> Module 4 <span class="box"></span></div></div>
  </div>

  <div class="office">
    <p class="form-heading">OFFICE USE ONLY:</p>
    <div class="field-line">Confirmation Sent:</div>
    <div class="field-line">Contact Person:</div>
    <div class="field-line">Invoice No.:</div>
    <div class="field-line">Paid:</div>
  </div>
</section>

</body>
</html>
```